Radio Service company needs ad for trade publication

Airwave Partners provides sales, content, production, technology, and promotion products and services to radio stations to help increase sales and solutions to improve operations and reduce costs. We are looking for a creative ad (sizes 720x250, 300x250, 728x180) with a theme around "MASTER YOUR 2024 BUDGET with AIRWAVE PARTNERS". Categories we have products/services to help them get budget into alignment. (1) Sales (2) Content & Programming (3) Technology (4) Production & Imaging (5) Promotions & Marketing (6) Support Services
"Don't go into the new year with an Unrealistic Budget.....We can Help!"

```html
<!DOCTYPE html>
<html lang="en">
<head>
<meta charset="utf-8">
<title>Airwave Partners – Budget Ad Set</title>
<link rel="stylesheet" href="https://fonts.googleapis.com/css2?family=Barlow+Condensed:wght@300;400;600;700&display=swap">
<style>
  :root {
    --canvas: #e3e3e3;
    --paper: #ffffff;
    --navy: #27399a;
    --royal: #24409b;
    --sky: #3a86d0;
    --sky-deep: #2b62b8;
    --steel-dark: #1f2126;
    --steel-mid: #4a4f59;
    --white: #ffffff;
  }
  * { margin: 0; padding: 0; box-sizing: border-box; }
  html, body { width: 851px; height: 1200px; overflow: hidden; background: var(--canvas); }
  body { font-family: "Barlow Condensed", "Arial Narrow", sans-serif; }

  .sheet {
    position: relative;
    width: 881px; height: 1242px;
    transform: scale(0.966);
    transform-origin: 0 0;
  }

  .ad { position: absolute; background: var(--paper); overflow: hidden; }
  .ad-art { position: absolute; inset: 0; width: 100%; height: 100%; }

  .brand {
    position: absolute;
    display: flex; align-items: center; gap: 6px;
    color: var(--sky-deep);
    font-weight: 700;
    line-height: 0.95;
    letter-spacing: 0.02em;
  }
  .brand-dot { border-radius: 50%; background: var(--sky); flex: none; }

  .headline {
    position: absolute;
    color: var(--navy);
    font-weight: 300;
  }
  .headline strong { font-weight: 600; }

  .cta {
    position: absolute;
    display: flex; align-items: center; justify-content: center;
    background: var(--royal);
    color: var(--white);
    border-radius: 999px;
    font-weight: 400;
    white-space: nowrap;
  }

  /* 720 x 250 */
  .ad-wide { left: 68px; top: 62px; width: 720px; height: 250px; }
  .ad-wide .brand { left: 32px; top: 22px; font-size: 24px; }
  .ad-wide .brand-dot { width: 14px; height: 14px; }
  .ad-wide .headline { left: 32px; top: 80px; width: 400px; font-size: 26px; line-height: 31px; }
  .ad-wide .cta { left: 28px; top: 191px; width: 173px; height: 39px; font-size: 17px; }

  /* 728-class leaderboard */
  .ad-strip { left: 60px; top: 367px; width: 736px; height: 120px; }
  .ad-strip .brand { left: 22px; top: 40px; font-size: 20px; }
  .ad-strip .brand-dot { width: 12px; height: 12px; }
  .ad-strip .headline { left: 151px; top: 24px; width: 310px; font-size: 20px; line-height: 26px; }
  .ad-strip .cta { left: 463px; top: 52px; width: 125px; height: 28px; font-size: 12.5px; border: 1px solid var(--white); }

  /* 300 x 250 */
  .ad-square { left: 68px; top: 572px; width: 300px; height: 250px; }
  .ad-square .brand { left: 18px; top: 22px; font-size: 19px; }
  .ad-square .brand-dot { width: 11px; height: 11px; }
  .ad-square .headline { left: 18px; top: 76px; width: 170px; font-size: 17px; line-height: 23.5px; }
  .ad-square .cta { left: 16px; top: 206px; width: 126px; height: 27px; font-size: 12.5px; }

  /* 160 x 600 */
  .ad-tower { left: 636px; top: 572px; width: 160px; height: 600px; }
  .ad-tower .brand { left: 22px; top: 322px; font-size: 20px; }
  .ad-tower .brand-dot { width: 11px; height: 11px; }
  .ad-tower .headline { left: 22px; top: 385px; width: 128px; font-size: 16.5px; line-height: 23.5px; }
  .ad-tower .cta { left: 23px; top: 547px; width: 124px; height: 27px; font-size: 12.5px; }
</style>
</head>
<body>
<main class="sheet">

  <section class="ad ad-wide" aria-label="Airwave Partners banner 720 by 250">
    <svg class="ad-art" viewBox="0 0 720 250" aria-hidden="true">
      <defs>
        <linearGradient id="skyWide" x1="0" y1="0" x2="1" y2="0">
          <stop offset="0" stop-color="#3f8fd6"/>
          <stop offset="1" stop-color="#2a5cb5"/>
        </linearGradient>
        <linearGradient id="micWide" x1="0" y1="0" x2="1" y2="1">
          <stop offset="0" stop-color="#5a5f69"/>
          <stop offset="1" stop-color="#1c1e23"/>
        </linearGradient>
      </defs>
      <rect x="560" y="0" width="160" height="250" fill="url(#skyWide)"/>
      <circle cx="600" cy="350" r="205" fill="var(--royal)"/>
      <circle cx="640" cy="20" r="120" fill="var(--paper)" opacity="0"/>
      <g role="img" aria-label="Studio condenser microphone in a shock mount">
        <path d="M470 0 H690 V250 H470 Z" fill="url(#micWide)" opacity="0.92"/>
      </g>
    </svg>
    <div class="brand"><span class="brand-dot"></span><span>AIRWAVE<br>PARTNERS</span></div>
    <p class="headline">Don't start the new year with budgeting stress. Let us help you craft a budget for <strong>success for your radio station!</strong></p>
    <span class="cta">Get Started Now</span>
  </section>

  <section class="ad ad-strip" aria-label="Airwave Partners leaderboard banner">
    <svg class="ad-art" viewBox="0 0 736 120" aria-hidden="true">
      <defs>
        <linearGradient id="micStrip" x1="0" y1="0" x2="1" y2="1">
          <stop offset="0" stop-color="#5a5f69"/>
          <stop offset="1" stop-color="#1c1e23"/>
        </linearGradient>
      </defs>
      <rect x="560" y="0" width="176" height="120" fill="#3a82cf"/>
      <circle cx="570" cy="200" r="130" fill="var(--royal)"/>
      <rect x="728" y="0" width="8" height="120" fill="var(--royal)"/>
      <g role="img" aria-label="Studio condenser microphone in a shock mount">
        <path d="M545 0 H728 V120 H545 Z" fill="url(#micStrip)" opacity="0.92"/>
      </g>
    </svg>
    <div class="brand"><span class="brand-dot"></span><span>AIRWAVE<br>PARTNERS</span></div>
    <p class="headline">Don't start the new year with budgeting stress. Let us help you craft a budget for <strong>success for your radio station</strong>!</p>
    <span class="cta">Get Started Now</span>
  </section>

  <section class="ad ad-square" aria-label="Airwave Partners banner 300 by 250">
    <svg class="ad-art" viewBox="0 0 300 250" aria-hidden="true">
      <defs>
        <linearGradient id="micSquare" x1="0" y1="0" x2="1" y2="1">
          <stop offset="0" stop-color="#5a5f69"/>
          <stop offset="1" stop-color="#1c1e23"/>
        </linearGradient>
      </defs>
      <circle cx="300" cy="125" r="110" fill="var(--sky)"/>
      <circle cx="200" cy="285" r="70" fill="var(--royal)"/>
      <g role="img" aria-label="Studio condenser microphone in a shock mount">
        <path d="M182 0 H300 V250 H182 Z" fill="url(#micSquare)" opacity="0.92"/>
      </g>
    </svg>
    <div class="brand"><span class="brand-dot"></span><span>AIRWAVE<br>PARTNERS</span></div>
    <p class="headline">Don't start the new year with budgeting stress. Let us help you craft a budget for <strong>success for your radio station!</strong></p>
    <span class="cta">Get Started Now</span>
  </section>

  <section class="ad ad-tower" aria-label="Airwave Partners skyscraper banner">
    <svg class="ad-art" viewBox="0 0 160 600" aria-hidden="true">
      <defs>
        <linearGradient id="micTower" x1="0" y1="0" x2="1" y2="1">
          <stop offset="0" stop-color="#5a5f69"/>
          <stop offset="1" stop-color="#1c1e23"/>
        </linearGradient>
      </defs>
      <rect x="0" y="0" width="160" height="294" fill="var(--paper)"/>
      <circle cx="60" cy="10" r="110" fill="var(--royal)"/>
      <circle cx="150" cy="150" r="145" fill="var(--sky)"/>
      <rect x="0" y="0" width="160" height="0" fill="none"/>
      <g role="img" aria-label="Studio condenser microphone in a shock mount">
        <path d="M10 0 H160 V294 H10 Z" fill="url(#micTower)" opacity="0.92"/>
      </g>
    </svg>
    <div class="brand"><span class="brand-dot"></span><span>AIRWAVE<br>PARTNERS</span></div>
    <p class="headline">Don't start the new year with budgeting stress. Let us help you craft a budget for <strong>success for your radio station!</strong></p>
    <span class="cta">Get Started Now</span>
  </section>

</main>
</body>
</html>
```